Design a "healthy, happy dog and cat" cheque/check background

I am looking for a few design concepts featuring a happy healthy dog and cat, that will be used as the background of a paper cheque/check.

This will require Photoshop and stock photos.

Here is the design brief: https://files.brivontel.net/sheet/48kQmZ2xTrWvLpN7aHcYeJ5uBdFsKo9GiRtXnVw3Lz/view?share=on

Colors

Designer to choose colors to be used in the design.

Requirements
Must have
• A happy dog and cat the main focus within the "empty" central part of the cheque/check, and a complementary background for the rest of the cheque, following the design guidelines in the attached google doc.

```html
<!DOCTYPE html>
<html lang="en">
<head>
<meta charset="utf-8">
<title>Personal Cheque – Dog and Cat Background</title>
<link rel="stylesheet" href="https://fonts.googleapis.com/css2?family=Arimo:wght@400;700&family=Share+Tech+Mono&display=swap">
<style>
  :root {
    --stage: #000000;
    --paper: #ffffff;
    --cheque-left: #f3f2bd;
    --cheque-mid: #f6dc98;
    --cheque-right: #f3a65a;
    --ink: #3a3a3a;
    --ink-dark: #111111;
    --rule: #333333;
    --field: #ffffff;
    --photo-light: #f1d29a;
    --photo-mid: #d9b17a;
    --photo-soft: #cfc6bd;
  }
  * { margin: 0; padding: 0; box-sizing: border-box; }
  html, body { width: 1200px; height: 1000px; overflow: hidden; background: var(--stage); }
  body { position: relative; font-family: "Arimo", Arial, sans-serif; color: var(--ink); }

  .sheet { position: absolute; left: 12px; top: 221px; width: 1178px; height: 534px; background: var(--paper); }
  .cheque {
    position: absolute; left: 24px; top: 19px; width: 1152px; height: 390px;
    background: linear-gradient(90deg, var(--cheque-left) 0%, var(--cheque-left) 38%, var(--cheque-mid) 55%, var(--cheque-right) 75%, var(--cheque-right) 100%);
  }
  .pet-photo {
    position: absolute; left: 340px; top: 10px; width: 470px; height: 380px;
    background: radial-gradient(ellipse at 50% 55%, var(--photo-mid) 0%, var(--photo-light) 45%, rgba(241,210,154,0) 72%),
                radial-gradient(ellipse at 78% 55%, var(--photo-soft) 0%, rgba(207,198,189,0) 45%);
  }
  .abs { position: absolute; white-space: nowrap; }

  .account-holder { left: 32px; top: 42px; font-size: 21px; line-height: 21px; }
  .account-holder .name { font-weight: 700; display: block; }
  .account-holder .line { display: block; font-size: 19px; line-height: 21px; }

  .cheque-number { left: 980px; top: 28px; font-size: 24px; font-weight: 700; color: var(--ink-dark); }
  .date-label { left: 744px; top: 90px; font-size: 20px; color: var(--ink-dark); }
  .date-boxes { left: 809px; top: 70px; display: flex; gap: 3px; }
  .date-box { width: 36px; height: 37px; background: var(--field); display: flex; justify-content: center; }
  .date-box span { margin-top: 41px; font-size: 14px; color: var(--ink-dark); }

  .payee-label { left: 32px; top: 168px; font-size: 14px; line-height: 14px; color: var(--ink-dark); }
  .dollar-sign { left: 906px; top: 163px; font-size: 30px; color: var(--ink-dark); }
  .amount-box { left: 931px; top: 153px; width: 189px; height: 47px; background: var(--field); }
  .dollars-label { left: 877px; top: 230px; font-size: 15px; color: var(--ink-dark); }

  .institution-mark { left: 40px; top: 270px; width: 70px; height: 70px; border-radius: 50%; background: var(--ink-dark); }
  .institution { left: 127px; top: 276px; font-size: 17px; line-height: 19px; color: var(--ink-dark); }
  .institution .name { font-weight: 700; display: block; font-size: 18px; }
  .institution .line { display: block; }

  .company-name { left: 770px; top: 309px; font-size: 14px; color: var(--ink-dark); }
  .memo-label { left: 36px; top: 358px; font-size: 12px; color: var(--ink-dark); }
  .security-badge { left: 1114px; top: 248px; width: 32px; height: 134px; border: 1px dashed var(--ink-dark); }

  .rules { position: absolute; left: 0; top: 0; }

  .micr-line { position: absolute; left: 62px; top: 437px; font-family: "Share Tech Mono", monospace; font-size: 32px; letter-spacing: 2px; color: var(--ink-dark); word-spacing: 14px; }
</style>
</head>
<body>
  <div class="sheet">
    <div class="cheque">
      <div class="pet-photo" role="img" aria-label="Photo of a golden puppy nuzzling a grey tabby kitten"></div>

      <svg class="rules" width="1152" height="390" viewBox="0 0 1152 390">
        <g stroke="var(--rule)" stroke-width="1.2" fill="none">
          <polyline points="32,200 880,200 880,165"/>
          <polyline points="32,252 860,252 872,217"/>
          <line x1="32" y1="372" x2="334" y2="372"/>
          <line x1="650" y1="372" x2="1054" y2="372"/>
        </g>
      </svg>

      <div class="abs account-holder">
        <span class="name">Maple Row Cheques Personal Cheque</span>
        <span class="line">48 Orchard Lane</span>
        <span class="line">Brampton, Ontario L6P 2K4</span>
      </div>

      <div class="abs cheque-number">101</div>
      <div class="abs date-label">DATE</div>
      <div class="abs date-boxes">
        <div class="date-box"><span>D</span></div>
        <div class="date-box"><span>D</span></div>
        <div class="date-box"><span>M</span></div>
        <div class="date-box"><span>M</span></div>
        <div class="date-box"><span>Y</span></div>
        <div class="date-box"><span>Y</span></div>
        <div class="date-box"><span>Y</span></div>
        <div class="date-box"><span>Y</span></div>
      </div>

      <div class="abs payee-label">PAY TO THE<br>ORDER OF</div>
      <div class="abs dollar-sign">$</div>
      <div class="abs amount-box"></div>
      <div class="abs dollars-label">100 DOLLARS</div>

      <div class="abs institution-mark"></div>
      <div class="abs institution">
        <span class="name">Your Financial Institution</span>
        <span class="line">200 Finance Avenue</span>
        <span class="line">Your City, Your Province A1B 2CS</span>
      </div>

      <div class="abs company-name">Optional Company Name</div>
      <div class="abs memo-label">MEMO</div>
      <div class="abs security-badge"></div>
    </div>

    <div class="micr-line">⑈101⑈ ⑆12345⑉678⑆ 12345⑉6789⑈</div>
  </div>
</body>
</html>
```